6 Coffee Label designs for coffee bags

Design for 14oz coffee bags from 6 different regions. Each bag - label to represent the flavors of each coffee from each country. Include our logo and make it a fun designs. Can be creative design with whimsical or pictures. Use flavor notes to create design and specifics from each origin. Each label must include Origin name. Size of label is 4x5 inch. In the must haves is the description of each origin. Each to have it's own design but also to have similarities too so customer would recognize it from the same company.

Requirements
Must have
• These elements are required on the design:
14oz, www.larkvaleroastworks.com, logo

the following attributes:
1. use word "Colombian" - design to represent these flavor notes: A balanced cup with flavors of chocolate, nuts and dried fruit sugar with notes of citrus

2. use word "Guatemalan" - design to represent these flavor notes: Bright acidity and a medium body are complemented by milk chocolate, caramel and almond flavors.

3. use word "Ethiopian" - design to represent these flavor notes: Enjoy a clean cup, bright acidity and floral notes. Find lively flavors of citrus, jasmine and cane sugar.

4. use word "Honduran" - design to represent these flavor notes: A fresh, clean cup with a bright acidity, medium body and notes of cocoa, green apple and lemongrass

5. use word "Kenyan"- design to represent these flavor notes: Expect a heavy body, with fruity, sweet and cocoa flavors

6. Design to have a space to write in the Origin (use word "Origin:" ) design to represent: to recognize women coffee farmers and promote gender equality in green coffee production

```html
<!DOCTYPE html>
<html lang="en">
<head>
<meta charset="utf-8">
<title>Colombian – Coffee Bag Label</title>
<link href="https://fonts.googleapis.com/css2?family=Yellowtail&family=Oswald:wght@500;600&family=Roboto:wght@300&display=swap" rel="stylesheet">
<style>
  :root {
    --page-bg: #e4e2df;
    --label-bg: #ffffff;
    --band-orange: #f1ab61;
    --title-orange: #f5b46c;
    --title-shadow: #3b2517;
    --brand-red: #a3364a;
    --text-light: #ffffff;
    --art-warm: #b08a74;
    --art-light: #ebe7e4;
  }
  * { margin: 0; padding: 0; box-sizing: border-box; }
  html, body {
    width: 1200px;
    height: 1027px;
    overflow: hidden;
    background: var(--page-bg);
  }
  .label {
    position: absolute;
    left: 300px;
    top: 14px;
    width: 600px;
    height: 1000px;
    background: var(--label-bg);
    overflow: hidden;
  }
  .band {
    position: absolute;
    left: 0;
    top: 0;
    width: 600px;
    height: 1000px;
  }
  .brand {
    position: absolute;
    left: 0;
    top: 300px;
    width: 600px;
    display: flex;
    justify-content: center;
    align-items: center;
    gap: 10px;
    font-family: "Oswald", sans-serif;
    font-weight: 500;
    font-size: 24px;
    letter-spacing: 1px;
    color: var(--brand-red);
  }
  .brand-dot {
    width: 14px;
    height: 14px;
    border-radius: 50%;
    background: var(--brand-red);
  }
  .origin-title {
    position: absolute;
    left: 0;
    top: 390px;
    width: 600px;
    text-align: center;
    font-family: "Yellowtail", cursive;
    font-weight: 400;
    font-size: 80px;
    line-height: 1;
    color: var(--title-orange);
    text-shadow: 3px 3px 0 var(--title-shadow);
  }
  .cup-illustration {
    position: absolute;
    left: 160px;
    top: 500px;
    width: 310px;
    height: 190px;
    border-radius: 18px;
    background: linear-gradient(180deg, var(--art-warm) 0%, var(--art-light) 100%);
  }
  .tagline {
    position: absolute;
    left: 0;
    top: 738px;
    width: 600px;
    text-align: center;
    font-family: "Oswald", sans-serif;
    font-weight: 600;
    font-size: 27px;
    letter-spacing: 0.5px;
    color: var(--text-light);
  }
  .size {
    position: absolute;
    left: 86px;
    top: 848px;
    font-family: "Roboto", sans-serif;
    font-weight: 300;
    font-size: 27px;
    color: var(--text-light);
  }
  .net-weight {
    position: absolute;
    right: 70px;
    top: 836px;
    font-family: "Roboto", sans-serif;
    font-weight: 300;
    font-size: 25px;
    color: var(--text-light);
  }
  .website {
    position: absolute;
    left: 0;
    top: 928px;
    width: 600px;
    text-align: center;
    font-family: "Roboto", sans-serif;
    font-weight: 300;
    font-size: 18px;
    letter-spacing: 0.5px;
    color: var(--brand-red);
  }
</style>
</head>
<body>
  <main class="label">
    <svg class="band" viewBox="0 0 600 1000" aria-hidden="true">
      <polygon points="42,665 552,513 552,905 42,905" fill="var(--band-orange)"/>
    </svg>

    <div class="brand">
      <span class="brand-dot"></span>
      <span class="brand-name">Larkvale Roastworks</span>
    </div>

    <h1 class="origin-title">Colombian</h1>

    <div class="cup-illustration" role="img" aria-label="Illustration of a cup of coffee with a chocolate splash on a saucer, with almonds and walnuts beside it"></div>

    <p class="tagline">PREMIER QUALITY COFFEE</p>
    <p class="size">14oz</p>
    <p class="net-weight">Nt Wt. 100g</p>
    <p class="website">www.larkvaleroastworks.com</p>
  </main>
</body>
</html>
```